Business Card Revision

Need to redesign my business cards for a new professional look. We are a courier company. You can go to www.qvrunners.com to see what we do. The trucks have an old company name (Sprout) on them but that is the company we are just now
changing the name.

Target Market(s)

Potential clients. We service the automotive, plumbing, printing, air freight industries as well as many others.

Industry/Entity Type

Business

Contact Information for Business Card

QVmotion
20864 Lark Fenmore Parkway
Cincinnati, Oh 45873

Thomas R. Wendall
President

tom@qvrunners.com

Main: (513) 555-0147

```html
<!DOCTYPE html>
<html lang="en">
<head>
<meta charset="utf-8">
<title>QV Runners – Business Card</title>
<link rel="stylesheet" href="https://fonts.googleapis.com/css2?family=Montserrat:wght@400;600;700;800&display=swap">
<style>
  :root {
    --backdrop: #474747;
    --paper: #f5f5f3;
    --blue: #1a8fd0;
    --blue-light: #29aae1;
    --blue-deep: #0e68ad;
    --green: #3fbf5a;
    --ink-white: #ffffff;
  }
  html, body {
    margin: 0;
    width: 1200px;
    height: 1023px;
    overflow: hidden;
    background: var(--backdrop);
    font-family: "Montserrat", Arial, sans-serif;
  }
  .card {
    position: absolute;
    left: 100px;
    top: 226px;
    width: 1000px;
    height: 571px;
    background: var(--paper);
    box-shadow: 0 20px 40px rgba(0,0,0,.35);
    overflow: hidden;
  }
  .card-art {
    position: absolute;
    inset: 0;
    width: 100%;
    height: 100%;
  }
  .brand-name {
    position: absolute;
    left: 370px;
    top: 38px;
    margin: 0;
    font-size: 62px;
    font-weight: 800;
    color: var(--blue);
    letter-spacing: 1px;
    line-height: 1;
    white-space: nowrap;
  }
  .person {
    position: absolute;
    left: 70px;
    top: 372px;
    color: var(--ink-white);
  }
  .person-name {
    margin: 0;
    font-size: 30px;
    font-weight: 700;
  }
  .person-role {
    margin: 2px 0 0;
    font-size: 13px;
    font-weight: 400;
  }
  .person-rule {
    width: 170px;
    height: 1px;
    background: rgba(255,255,255,.75);
    margin: 14px 0 12px;
  }
  .contact-list {
    list-style: none;
    margin: 0;
    padding: 0;
    font-size: 17px;
    font-weight: 600;
  }
  .contact-list li {
    display: flex;
    align-items: center;
    gap: 12px;
    height: 30px;
  }
  .contact-icon { width: 18px; height: 18px; flex: none; }
  .office {
    position: absolute;
    left: 650px;
    top: 282px;
    color: var(--ink-white);
  }
  .office-name {
    margin: 0 0 8px;
    font-size: 25px;
    font-weight: 700;
  }
  .office-address {
    display: flex;
    gap: 12px;
    font-style: normal;
    font-size: 17px;
    font-weight: 600;
    line-height: 1.35;
  }
  .office-icon { width: 20px; height: 20px; margin-top: 2px; flex: none; }
</style>
</head>
<body>
  <article class="card">
    <svg class="card-art" viewBox="0 0 1000 571" aria-hidden="true">
      <defs>
        <linearGradient id="bandFill" x1="0" y1="0" x2="1" y2="1">
          <stop offset="0" stop-color="var(--blue-light)"/>
          <stop offset="0.6" stop-color="var(--blue)"/>
          <stop offset="1" stop-color="var(--blue-deep)"/>
        </linearGradient>
      </defs>
      <path class="band-edge" fill="var(--green)"
            d="M0,326 C230,346 380,270 540,200 S830,118 1000,124 L1000,571 L0,571 Z"/>
      <path class="band" fill="url(#bandFill)"
            d="M0,344 C230,364 380,288 540,218 S830,136 1000,142 L1000,571 L0,571 Z"/>
    </svg>

    <h1 class="brand-name">QV Runners</h1>

    <section class="person">
      <h2 class="person-name">Thomas R. Wendall</h2>
      <p class="person-role">President</p>
      <div class="person-rule"></div>
      <ul class="contact-list">
        <li>
          <svg class="contact-icon" viewBox="0 0 24 24" fill="#fff"><path d="M6.6 10.8a15 15 0 0 0 6.6 6.6l2.2-2.2a1 1 0 0 1 1-.25 11.4 11.4 0 0 0 3.6.57 1 1 0 0 1 1 1V20a1 1 0 0 1-1 1A17 17 0 0 1 3 4a1 1 0 0 1 1-1h3.5a1 1 0 0 1 1 1c0 1.25.2 2.45.57 3.57a1 1 0 0 1-.25 1z"/></svg>
          (513) 555-0147
        </li>
        <li>
          <svg class="contact-icon" viewBox="0 0 24 24" fill="#fff"><path d="M2 5h20v14H2z M4 7v.5l8 5 8-5V7l-8 5z" fill-rule="evenodd"/></svg>
          tom@qvrunners.com
        </li>
        <li>
          <svg class="contact-icon" viewBox="0 0 24 24" fill="none" stroke="#fff" stroke-width="2"><circle cx="12" cy="12" r="9"/><path d="M3 12h18M12 3c3 3 3 15 0 18M12 3c-3 3-3 15 0 18"/></svg>
          www.qvrunners.com
        </li>
      </ul>
    </section>

    <section class="office">
      <h3 class="office-name">QVmotion</h3>
      <address class="office-address">
        <svg class="office-icon" viewBox="0 0 24 24" fill="#fff"><path d="M12 2 2 12h5v9h10v-9h5z"/></svg>
        <span>20864 Lark Fenmore Parkway<br>Cincinnati, Oh 45873</span>
      </address>
    </section>
  </article>
</body>
</html>
```